Business Card

I need a business card for my work as an energy lawyer. I am a single prctioner and I consult to energy companies regarding a variety of legal issues involving environmental matters, energy efficiency, regulations and contractual arrangements. i need a distinctive business card that stands out and is easy to read. I like bold colors or high contrast. I like a sparse architectural design. The font should be easy to read (many of my clients use reading glasses and are concerned about small type). The card should communicate that I am somewhat different from ordinary legal counsel. Below are some examples of cards that I like. Thank you for your interest and thought. Glen Dusty Harlow
Updates

Thanks to everyone who has submitted a design.  My general comments are:

1.  I like the colourful cards and the high contrast cards.
2.  I prefer the use of icons for home address, phone, mobile and email.
3.  For the high contrast cards please use three colours - black background, and red and white for the logo or information.
4.  The mobile number area code should be 403 and not 404.
5.  I also need to add a direct phone line which is 555-318-2967.

Thank you,

Glen Harlow

Project Deadline Extended
Reason: I have briefly extended the deadline by three days to allow those individuals who responded early to revise their designs based upon the subsequent clarification of the colours (red, white, black background) and the request to use icons and add a direct phone number.

Industry/Entity Type

Business

```html
<!DOCTYPE html>
<html lang="en">
<head>
<meta charset="utf-8">
<title>Glen Dusty Harlow – Business Card</title>
<link rel="stylesheet" href="https://fonts.googleapis.com/css2?family=Poppins:wght@600&family=Source+Sans+3:wght@400;700&display=swap">
<style>
  :root {
    --orange: #f58220;
    --orange-light: #f7a21b;
    --amber: #f9c23c;
    --white: #ffffff;
    --ink: #3a3a3a;
    --icon-blue: #1d6fb8;
    --grey-bg: #e6e6e6;
    --shadow: rgba(0, 0, 0, 0.18);
  }
  * { box-sizing: border-box; margin: 0; padding: 0; }
  html, body { width: 1200px; height: 900px; overflow: hidden; }
  body {
    background: var(--grey-bg);
    position: relative;
    font-family: "Source Sans 3", sans-serif;
  }
  .card {
    position: absolute;
    width: 520px;
    height: 297px;
    overflow: hidden;
    box-shadow: 0 10px 24px var(--shadow);
  }

  /* Front */
  .card-front {
    left: 70px; top: 140px;
    background: var(--orange);
    display: flex; flex-direction: column;
    align-items: center; justify-content: center;
    gap: 16px;
  }
  .brand {
    display: flex; align-items: center; gap: 10px;
    color: var(--white);
    font-family: "Poppins", sans-serif;
    font-weight: 600;
    font-size: 26px;
    letter-spacing: 1px;
  }
  .brand-dot {
    width: 34px; height: 34px;
    border-radius: 50%;
    background: var(--white);
  }
  .front-name {
    color: var(--white);
    font-family: "Poppins", sans-serif;
    font-weight: 600;
    font-size: 36px;
  }

  /* Back */
  .card-back {
    left: 610px; top: 440px;
    background: var(--white);
  }
  .band { position: absolute; display: flex; gap: 8px; }
  .band-top { left: 0; top: 0; width: 100%; height: 22px; }
  .band-mid { right: 0; top: 128px; width: 250px; height: 22px; }
  .band-bottom { left: 0; bottom: 0; width: 100%; height: 28px; background: var(--orange-light); }
  .band-block { height: 100%; background: var(--orange-light); }
  .band-block.main { flex: 1; }
  .band-block.short { width: 40px; background: var(--amber); }
  .band-mid .band-block { background: var(--orange); }
  .band-mid .band-block.short { background: var(--amber); }

  .back-brand {
    position: absolute; right: 24px; top: 40px;
    display: flex; align-items: center; gap: 6px;
    color: var(--orange);
    font-family: "Poppins", sans-serif;
    font-weight: 600;
    font-size: 20px;
  }
  .back-brand .brand-dot { width: 22px; height: 22px; background: var(--orange); }

  .contact { position: absolute; left: 36px; top: 120px; }
  .contact-name {
    color: var(--orange);
    font-weight: 700;
    font-size: 22px;
    line-height: 1.1;
  }
  .contact-title {
    color: var(--ink);
    font-size: 14px;
    margin-bottom: 8px;
  }
  .contact-list { list-style: none; }
  .contact-list li {
    display: flex; align-items: flex-start; gap: 8px;
    color: var(--ink);
    font-size: 14px;
    line-height: 1.2;
    margin-bottom: 4px;
  }
  .contact-list svg { flex: none; width: 16px; height: 16px; margin-top: 1px; }
</style>
</head>
<body>

  <section class="card card-front" aria-label="Business card front">
    <div class="brand"><span class="brand-dot"></span>GDH</div>
    <h1 class="front-name">Glen Dusty Harlow</h1>
  </section>

  <section class="card card-back" aria-label="Business card back">
    <div class="band band-top">
      <span class="band-block short"></span>
      <span class="band-block short"></span>
      <span class="band-block main"></span>
    </div>

    <div class="back-brand"><span class="brand-dot"></span>GDH</div>

    <div class="band band-mid">
      <span class="band-block main"></span>
      <span class="band-block short"></span>
    </div>

    <div class="contact">
      <h2 class="contact-name">Glen Dusty Harlow</h2>
      <p class="contact-title">Energy and Regulatory Counsel, JD</p>
      <ul class="contact-list">
        <li>
          <svg viewBox="0 0 16 16" aria-hidden="true"><path d="M8 1 L15 8 H13 V15 H9.5 V10.5 H6.5 V15 H3 V8 H1 Z" fill="#2b2b2b"/></svg>
          418 Fennell Road, Harrow Bay, Eastland
        </li>
        <li>
          <svg viewBox="0 0 16 16" aria-hidden="true"><circle cx="8" cy="8" r="7.2" fill="#ffffff" stroke="#1d6fb8" stroke-width="1.4"/><path d="M5.3 4.2 L6.6 5.6 L5.9 6.7 Q6.8 8.6 9.3 10.1 L10.4 9.4 L11.8 10.7 L10.9 12 Q7.4 11.8 4.1 5.2 Z" fill="#1d6fb8"/></svg>
          <span>1 555 627 4109<br>1 555 893 2046</span>
        </li>
        <li>
          <svg viewBox="0 0 16 16" aria-hidden="true"><rect x="1.5" y="3.5" width="13" height="9" rx="1" fill="#ffffff" stroke="#1d6fb8" stroke-width="1.2"/><path d="M1.8 4 L8 9 L14.2 4" fill="none" stroke="#1d6fb8" stroke-width="1.2"/></svg>
          office@fennellcounsel.com
        </li>
      </ul>
    </div>

    <div class="band band-bottom"></div>
  </section>

</body>
</html>
```